Business card for our large format printing and installation business

We want a professional looking business card for our business. We manufacture and install Signs.

On the back of the card add this info
Large Format Graphics Printing & Installations, Event Graphics, Banners, Posters, Vehicle Fleet Graphics, Boat Wraps, Wall Murals, Decals,Displays,Signs,Plaques,Digital Signs

On the Front of the card add the Tallowfern Signs logo, plus On the back of the card add the Orange Tallowfern Wraps logo. The 2 vector logos are attached to the design brief.

Target Market(s)

Local business owners

Contact Information for Business Card

Colors
f37122
f68d4e
f9ba93

Requirements
Must have
• On the Front of the card add the Tallowfern Signs logo, plus On the back of the card add the Orange Tallowfern Wraps logo. The 2 vector logos are attached to the design brief.

```html
<!DOCTYPE html>
<html lang="en">
<head>
<meta charset="utf-8">
<title>Tallowfern Business Card</title>
<link rel="stylesheet" href="https://fonts.googleapis.com/css2?family=Lato:wght@400;700;900&display=swap">
<style>
  :root {
    --canvas: #6b6b6b;
    --card-black: #050505;
    --card-white: #ffffff;
    --accent: #f7a11c;
    --accent-deep: #f37122;
    --accent-light: #fdd23a;
    --text-light: #ffffff;
  }
  * { box-sizing: border-box; margin: 0; padding: 0; }
  html, body {
    width: 1200px; height: 1200px; overflow: hidden;
    background: var(--canvas);
    font-family: "Lato", sans-serif;
  }
  .card {
    position: absolute; left: 240px; width: 720px; height: 418px;
    border-radius: 26px; overflow: hidden; background: var(--card-black);
  }
  .card-front { top: 142px; }
  .card-back { top: 640px; }
  .front-shape { position: absolute; inset: 0; }
  .holder { position: absolute; left: 36px; top: 60px; }
  .holder-name { color: var(--accent); font-weight: 700; font-size: 29px; line-height: 1.1; }
  .holder-title { color: var(--text-light); font-size: 16px; margin-top: 4px; }
  .address {
    position: absolute; left: 32px; top: 205px;
    color: var(--text-light); font-size: 16.5px; line-height: 1.3;
  }
  .contact-list {
    position: absolute; left: 32px; top: 266px; list-style: none;
    color: var(--text-light); font-size: 16.5px;
  }
  .contact-item { display: flex; align-items: center; gap: 14px; height: 25px; }
  .contact-icon { width: 15px; height: 15px; flex: none; }
  .brand-front {
    position: absolute; left: 370px; right: 0; top: 0; bottom: 0;
    display: flex; flex-direction: column; align-items: center; justify-content: center;
    color: var(--accent-deep); font-weight: 900; line-height: 0.95;
  }
  .brand-front .brand-main { font-size: 50px; }
  .brand-front .brand-sub { font-size: 36px; margin-left: 120px; }
  .brand-back {
    position: absolute; left: 0; right: 0; top: 108px;
    display: flex; flex-direction: column; align-items: center;
    color: var(--accent); font-weight: 900; line-height: 0.95;
  }
  .brand-back .brand-main { font-size: 86px; }
  .brand-back .brand-sub { font-size: 56px; margin-left: 170px; }
  .services {
    position: absolute; left: 0; right: 0; top: 318px;
    text-align: center; color: var(--text-light); font-size: 19px; line-height: 1.3;
  }
  .sep { color: var(--accent); margin: 0 4px; }
</style>
</head>
<body>
  <section class="card card-front">
    <svg class="front-shape" viewBox="0 0 720 418" width="720" height="418" aria-hidden="true">
      <defs>
        <linearGradient id="edgeGlow" x1="0" y1="0" x2="0" y2="1">
          <stop offset="0" stop-color="#fdd23a"/>
          <stop offset="1" stop-color="#f37122"/>
        </linearGradient>
      </defs>
      <path d="M396 0 C 310 90, 310 320, 396 418 L 720 418 L 720 0 Z" fill="url(#edgeGlow)"/>
      <path d="M404 0 C 322 90, 322 320, 404 418 L 720 418 L 720 0 Z" fill="#ffffff"/>
    </svg>

    <div class="holder">
      <p class="holder-name">Marcus Ellery</p>
      <p class="holder-title">Founder &amp; CEO</p>
    </div>

    <p class="address">1480 Harbor Mill Lane #7<br>Port Alder, FL 33120</p>

    <ul class="contact-list">
      <li class="contact-item">
        <svg class="contact-icon" viewBox="0 0 16 16"><path d="M3 1h3l1.5 4-2 1.3a8 8 0 0 0 4.2 4.2L11 8.5l4 1.5v3a2 2 0 0 1-2 2A12 12 0 0 1 1 3a2 2 0 0 1 2-2z" fill="none" stroke="#f7a11c" stroke-width="1.5"/></svg>
        <span>555-310-4827 (Office)</span>
      </li>
      <li class="contact-item">
        <svg class="contact-icon" viewBox="0 0 16 16"><path d="M3 1h3l1.5 4-2 1.3a8 8 0 0 0 4.2 4.2L11 8.5l4 1.5v3a2 2 0 0 1-2 2A12 12 0 0 1 1 3a2 2 0 0 1 2-2z" fill="none" stroke="#f7a11c" stroke-width="1.5"/></svg>
        <span>555-642-1905 (Direct)</span>
      </li>
      <li class="contact-item">
        <svg class="contact-icon" viewBox="0 0 16 16"><rect x="1" y="3" width="14" height="10" fill="#f7a11c"/><path d="M1 3l7 6 7-6" fill="none" stroke="#050505" stroke-width="1.3"/></svg>
        <span>marcus@tallowfern.net</span>
      </li>
      <li class="contact-item">
        <svg class="contact-icon" viewBox="0 0 16 16"><g fill="none" stroke="#f7a11c" stroke-width="1.3"><circle cx="8" cy="8" r="6.5"/><ellipse cx="8" cy="8" rx="3" ry="6.5"/><path d="M1.5 8h13M2.5 5h11M2.5 11h11"/></g></svg>
        <span>www.tallowfernwraps.com</span>
      </li>
    </ul>

    <div class="brand-front">
      <span class="brand-main">Tallowfern</span>
      <span class="brand-sub">Signs</span>
    </div>
  </section>

  <section class="card card-back">
    <div class="brand-back">
      <span class="brand-main">Tallowfern</span>
      <span class="brand-sub">Wraps</span>
    </div>
    <p class="services">
      Large Format Graphics Printing &amp; Installations<br>
      Banners<span class="sep">•</span>Posters<span class="sep">•</span>Vehicle Graphics<span class="sep">•</span>Boat Wraps<span class="sep">•</span>Wall Murals<br>
      Decals<span class="sep">•</span>Displays<span class="sep">•</span>Signs<span class="sep">•</span>Plaques<span class="sep">•</span>Digital Signs
    </p>
  </section>
</body>
</html>
```